Postcard Design

I run a kitchen cabinet company that sells pre-manufactured cabinets, specially made by Brindlewood Cabinets. You can see their website at brindlewoodcabinets-example.com and my website at thelarchbenchco-example.com. In addition to selling cabinets I sell counter tops (laminate and granite) along with appliances.

I need a postcard design that will be targeted at new home owners who recently purchased their property and may need kitchen cabinets, counter tops and/or appliances. I do not need a list of new home owners, I will have that.

My 'shtick' is I offer FREE Delivery and FREE Installation.
When I talk to customers about pricing I routinely come in 20-30% cheaper than the big box stores.

New Home Owners - not new construction

It Company

```html
<!DOCTYPE html>
<html lang="en">
<head>
<meta charset="utf-8">
<title>The Larch Bench Co. – Postcard</title>
<link rel="stylesheet" href="https://fonts.googleapis.com/css2?family=Barlow:wght@400;500;600&display=swap">
<style>
  :root {
    --page: #1f1f1f;
    --card-white: #ffffff;
    --charcoal: #3c3c3e;
    --charcoal-dark: #2a2a2c;
    --red: #8e2722;
    --red-light: #a8332b;
    --ink: #333333;
    --light-grey: #dcdcdc;
    --text-light: #f2f2f2;
    --photo-wood: #9a5f36;
    --photo-wall: #d9a37c;
    --photo-orange: #e49a5c;
    --photo-cabinet: #3b3a3c;
  }
  * { box-sizing: border-box; margin: 0; padding: 0; }
  html, body { width: 1200px; height: 1200px; overflow: hidden; }
  body {
    background: var(--page);
    font-family: "Barlow", Arial, sans-serif;
    position: relative;
  }
  .postcard {
    position: absolute;
    left: 220px;
    width: 760px;
    height: 490px;
    overflow: hidden;
  }

  /* ---------- Mailing side ---------- */
  .mailing-side { top: 70px; background: var(--card-white); }
  .mailing-side .brand {
    position: absolute; left: 36px; top: 26px;
    font-size: 28px; font-weight: 600; color: var(--ink); letter-spacing: 0.5px;
  }
  .mailing-side .address {
    position: absolute; left: 300px; top: 38px;
    font-size: 13px; font-weight: 500; color: var(--red);
  }
  .mailing-side .photo {
    position: absolute; left: 36px; top: 66px; width: 490px; height: 190px;
    background: linear-gradient(180deg, var(--photo-wood) 0%, #b57a4c 55%, var(--photo-wall) 100%);
  }
  .mailing-side .intro {
    position: absolute; left: 36px; top: 256px; width: 490px; height: 156px;
    background: var(--charcoal);
    color: var(--text-light);
    font-size: 13.4px; line-height: 1.42; padding: 26px 18px 0 20px;
  }
  .mailing-side .price-band {
    position: absolute; left: 14px; top: 412px; width: 512px; height: 50px;
    background: linear-gradient(180deg, var(--red-light), var(--red));
    color: #fff; font-size: 22px; padding: 11px 0 0 30px;
  }
  .mailing-side .stamp-box {
    position: absolute; left: 636px; top: 72px; width: 104px; height: 110px;
    border: 1px solid #9a9a9a;
  }

  /* ---------- Promo side ---------- */
  .promo-side { top: 620px; background: var(--charcoal); }
  .promo-side .side-panel {
    position: absolute; left: 0; top: 0; width: 290px; height: 400px;
    background: linear-gradient(180deg, var(--charcoal-dark), var(--charcoal) 60%, #4a4a4c);
  }
  .promo-side .photo {
    position: absolute; left: 290px; top: 0; width: 470px; height: 400px;
    background: linear-gradient(180deg, #f1e6da 0%, var(--photo-orange) 30%, var(--photo-cabinet) 55%, #6b4b3a 100%);
  }
  .promo-side .headline {
    position: absolute; left: 0; top: 36px; width: 300px; height: 118px;
    background: linear-gradient(180deg, var(--red-light), var(--red));
    color: #fff; text-align: center; padding-top: 10px;
  }
  .headline .lead { font-size: 20px; font-weight: 400; }
  .headline .feature { font-size: 42px; font-weight: 400; line-height: 1.05; }
  .headline .follow { font-size: 20px; font-weight: 500; }
  .promo-side .services {
    position: absolute; left: 14px; top: 170px; list-style: none;
  }
  .services li {
    display: flex; align-items: center; gap: 10px;
    color: var(--text-light); font-size: 19px; height: 31.5px;
  }
  .services svg { width: 14px; height: 14px; flex: none; }
  .promo-side .footer-brand {
    position: absolute; left: 0; top: 412px; width: 290px; height: 66px;
    background: linear-gradient(180deg, #f4f4f4, var(--light-grey));
    color: var(--ink); font-size: 28px; font-weight: 600;
    display: flex; align-items: center; justify-content: center; letter-spacing: 0.3px;
  }
  .promo-side .footer-offer {
    position: absolute; left: 290px; top: 412px; width: 470px; height: 66px;
    background: linear-gradient(180deg, var(--red-light), var(--red));
    color: #fff; text-align: center; padding-top: 7px;
  }
  .footer-offer .offer { font-size: 24px; font-weight: 600; }
  .footer-offer .contact { font-size: 12px; color: #f0d6d3; margin-top: 2px; }
  .footer-offer .contact strong { font-size: 15px; font-weight: 500; color: #fff; }
  .promo-side .base-strip {
    position: absolute; left: 0; top: 478px; width: 760px; height: 12px; background: var(--charcoal);
  }
</style>
</head>
<body>

<section class="postcard mailing-side">
  <div class="brand">The Larch Bench Co.</div>
  <div class="address">4480 W Alder Ln, Fenmoor MN 55990</div>
  <div class="photo" role="img" aria-label="Photo of an installer measuring wooden upper kitchen cabinets"></div>
  <p class="intro">Bathroom &amp; kitchen cabinets for the entire Twin Cities MN metro and the surrounding metro area - Cabinet products and cabinet installation. Get the best deal on either one with our weekly and monthly specials and price breaks on orders of kitchen or bathroom cabinets including the installation - The Twin Cities cabinets pro!</p>
  <div class="price-band">20-30% cheaper than the big box stores</div>
  <div class="stamp-box"></div>
</section>

<section class="postcard promo-side">
  <div class="side-panel"></div>
  <div class="photo" role="img" aria-label="Photo of a modern kitchen with dark espresso cabinets, light countertops and orange walls"></div>
  <div class="headline">
    <div class="lead">Your Twin Cities Choice for</div>
    <div class="feature">Beautiful</div>
    <div class="follow">Cabinets/Countertops!</div>
  </div>
  <ul class="services">
    <li><svg viewBox="0 0 14 14"><rect x="0.5" y="0.5" width="13" height="13" fill="none" stroke="#a8332b"/><path d="M3 7l3 3 5-6" fill="none" stroke="#c0392b" stroke-width="1.8"/></svg>Kitchen Cabinets</li>
    <li><svg viewBox="0 0 14 14"><rect x="0.5" y="0.5" width="13" height="13" fill="none" stroke="#a8332b"/><path d="M3 7l3 3 5-6" fill="none" stroke="#c0392b" stroke-width="1.8"/></svg>Bathroom Cabinets</li>
    <li><svg viewBox="0 0 14 14"><rect x="0.5" y="0.5" width="13" height="13" fill="none" stroke="#a8332b"/><path d="M3 7l3 3 5-6" fill="none" stroke="#c0392b" stroke-width="1.8"/></svg>Countertops</li>
    <li><svg viewBox="0 0 14 14"><rect x="0.5" y="0.5" width="13" height="13" fill="none" stroke="#a8332b"/><path d="M3 7l3 3 5-6" fill="none" stroke="#c0392b" stroke-width="1.8"/></svg>Maplecrest Appliances</li>
    <li><svg viewBox="0 0 14 14"><rect x="0.5" y="0.5" width="13" height="13" fill="none" stroke="#a8332b"/><path d="M3 7l3 3 5-6" fill="none" stroke="#c0392b" stroke-width="1.8"/></svg>Quality Installation</li>
    <li><svg viewBox="0 0 14 14"><rect x="0.5" y="0.5" width="13" height="13" fill="none" stroke="#a8332b"/><path d="M3 7l3 3 5-6" fill="none" stroke="#c0392b" stroke-width="1.8"/></svg>Dependable Workmanship</li>
  </ul>
  <div class="footer-brand">The Larch Bench Co.</div>
  <div class="footer-offer">
    <div class="offer">FREE Delivery and FREE Installation</div>
    <div class="contact">Visit us at: <strong>thelarchbenchco-example.com</strong> or Call us today: <strong>555-014-2276</strong></div>
  </div>
  <div class="base-strip"></div>
</section>

</body>
</html>
```